Commercial Real Estate Appraisal Company needs a postcard design

We need a postcard design for a commercial real estate company based out of Ballston Lake, New York called "Harborline Appraisers".

Harborline Appraisers, LLC., provides high quality commercial appraisal and real estate consulting services to our clients. Our company provides appraisal services for financial lending institutions, real estate developers, local municipalities, attorney’s, private individuals and businesses. Significant capital expenditures were made to ensure we can provide top of the line data research and research publications, as well as, generate our reports with industry leading appraisal software for increased accuracy and efficiency.

Services we provide

Advisory & Consulting Services, Net Lease Valuation, Capitalization Rate Consultation, Operating Expense Consultation, Discounted Cash Flow Analysis, Portfolio Valuation, Expert Witness Services, Property and Comparable Analyses, Financial Feasibility Studies, Property Tax Services, Going Concern Valuations, Real Estate Due Diligence Analyses, Highest and Best Use Studies, Real Estate Valuation, Lease Versus Purchase Analyses, Rent Arbitration and Consultation, Market Rent Analyses, Sale Lease-Backs Analysis, Market Studies, Site Inspections, Divorce Proceedings, Probate / Estate Matters

Please save room on the card for postage and addressing

Industry/Entity Type

Real Estate

```html
<!DOCTYPE html>
<html lang="en">
<head>
<meta charset="utf-8">
<title>Harborline Appraisers – Postcard</title>
<link rel="stylesheet" href="https://fonts.googleapis.com/css2?family=Roboto:wght@300;400;500&family=Bebas+Neue&display=swap">
<style>
  :root {
    --backdrop: #d9d9d9;
    --paper: #ffffff;
    --navy: #14254a;
    --navy-deep: #0f1c3a;
    --blueprint-a: #1c2b4e;
    --blueprint-b: #5b6a88;
    --stripe-light: #e6e7ea;
    --stripe-dark: #9fa3ab;
    --ink-light: #ffffff;
    --brand-ink: #1c2b4e;
  }
  * { margin: 0; padding: 0; box-sizing: border-box; }
  html, body {
    width: 1200px; height: 900px; overflow: hidden;
    background: var(--backdrop);
  }
  .postcard {
    position: absolute; left: 182px; top: 175px;
    width: 848px; height: 550px;
    overflow: hidden;
    background: var(--paper);
    font-family: "Roboto", Arial, sans-serif;
  }
  .postcard-art { position: absolute; inset: 0; width: 848px; height: 550px; }

  .brand {
    position: absolute; left: 36px; top: 118px; width: 230px;
    text-align: center; color: var(--brand-ink);
  }
  .brand-mark {
    display: block; width: 14px; height: 14px; margin: 0 auto 10px;
    background: var(--brand-ink);
  }
  .brand-name {
    font-family: "Roboto", Arial, sans-serif;
    font-weight: 500; font-size: 19px; letter-spacing: 0.5px;
    text-transform: uppercase;
  }
  .brand-tagline {
    margin-top: 3px;
    font-size: 8px; letter-spacing: 1.2px; text-transform: uppercase;
  }

  .pitch {
    position: absolute; right: 30px; top: 178px;
    color: var(--ink-light); text-align: right; line-height: 1;
  }
  .pitch-lead { font-weight: 300; font-size: 50px; }
  .pitch-big {
    font-family: "Bebas Neue", Impact, sans-serif;
    font-size: 64px; letter-spacing: 1px; margin-top: 4px;
  }
  .pitch-service { font-weight: 300; font-size: 29px; margin-top: 4px; }
  .pitch-row { display: flex; justify-content: flex-end; align-items: flex-end; }
  .pitch-leading {
    font-family: "Bebas Neue", Impact, sans-serif;
    font-size: 52px; margin-top: 4px; margin-right: 6px;
  }
  .pitch-stack { font-weight: 300; font-size: 22px; line-height: 0.95; text-align: center; padding-bottom: 4px; }
  .pitch-small { font-weight: 400; font-size: 14px; margin-right: 10px; padding-bottom: 8px; }
  .pitch-accuracy { font-weight: 300; font-size: 38px; }
  .pitch-efficiency { font-weight: 300; font-size: 56px; margin-top: -4px; }
</style>
</head>
<body>
  <main class="postcard">
    <svg class="postcard-art" viewBox="0 0 848 550" aria-hidden="false">
      <defs>
        <linearGradient id="blueprint" x1="0" y1="1" x2="1" y2="0">
          <stop offset="0" stop-color="var(--blueprint-a)"/>
          <stop offset="0.55" stop-color="var(--blueprint-b)"/>
          <stop offset="1" stop-color="var(--blueprint-a)"/>
        </linearGradient>
        <linearGradient id="stripe" x1="0" y1="1" x2="1" y2="0">
          <stop offset="0" stop-color="var(--stripe-light)"/>
          <stop offset="1" stop-color="var(--stripe-dark)"/>
        </linearGradient>
      </defs>
      <rect class="hero-photo" x="0" y="0" width="848" height="550" fill="url(#blueprint)"
            role="img" aria-label="Photo of a professional sketching a white-line house blueprint on a glass panel"/>
      <polygon class="corner-white" points="0,0 468,0 0,380" fill="var(--paper)"/>
      <polygon class="accent-stripe" points="148,550 848,0 848,10 218,550" fill="url(#stripe)"/>
      <polygon class="navy-panel" points="218,550 848,10 848,550" fill="var(--navy)"/>
    </svg>

    <div class="brand">
      <span class="brand-mark"></span>
      <div class="brand-name">Harborline Appraisers</div>
      <div class="brand-tagline">Real Estate Appraisers &amp; Consultants</div>
    </div>

    <div class="pitch">
      <div class="pitch-lead">High</div>
      <div class="pitch-big">QUALITY</div>
      <div class="pitch-service">commercial appraisal</div>
      <div class="pitch-service">real estate consulting</div>
      <div class="pitch-row">
        <span class="pitch-leading">LEADING</span>
        <span class="pitch-stack">appraisal<br>software</span>
      </div>
      <div class="pitch-row">
        <span class="pitch-small">for increased</span>
        <span class="pitch-accuracy">accuracy</span>
      </div>
      <div class="pitch-efficiency">efficiency</div>
    </div>
  </main>
</body>
</html>
```